Modern Email Signature & Alert Email Template

We are a car leasing company and are looking for a revamp to our emails. We would like a more modern & sleek presentation when we are emailing our clients. We would like a signature for our employees & a general template for notifications e.g. Lease Ending.

Would like to be able to copy & paste the email formatting to outlook & to our notification sending system.

Attached is our logo & the alert email that we send out.

Industry/Entity Type

Car Leasing

Colors

Designer to choose colors to be used in the design.

Requirements
Must have
• Our logo & Contact information

```html
<!DOCTYPE html>
<html lang="en">
<head>
<meta charset="utf-8">
<title>Tidewell Auto Leasing — Email Signature</title>
<link href="https://fonts.googleapis.com/css2?family=Nunito+Sans:wght@400;800&display=swap" rel="stylesheet">
<style>
  :root {
    --backdrop: #808080;
    --card: #ffffff;
    --brand-blue: #0a4fc9;
    --text: #3a3a3a;
    --band: #e4e5e7;
  }
  * { margin: 0; padding: 0; box-sizing: border-box; }
  html, body { width: 1200px; height: 1200px; overflow: hidden; }
  body {
    background: var(--backdrop);
    font-family: "Nunito Sans", Arial, sans-serif;
    color: var(--text);
    position: relative;
  }
  .signature {
    position: absolute;
    left: 122px; top: 445px;
    width: 956px; height: 295px;
    background: var(--card);
  }
  .brand {
    position: absolute;
    left: 44px; top: 76px;
    width: 254px;
    display: flex;
    align-items: center;
    gap: 9px;
  }
  .brand-dot {
    width: 16px; height: 16px;
    border-radius: 50%;
    background: var(--brand-blue);
    flex: none;
  }
  .brand-name {
    color: var(--brand-blue);
    font-weight: 800;
    font-size: 21px;
    line-height: 1;
    white-space: nowrap;
  }
  .role {
    position: absolute;
    left: 321px; top: 74px;
  }
  .role-title {
    color: var(--brand-blue);
    font-weight: 800;
    font-size: 20px;
    line-height: 1.2;
  }
  .role-company {
    margin-top: 4px;
    font-size: 16px;
  }
  .divider {
    position: absolute;
    top: 73px; width: 1.5px; height: 61px;
    background: var(--brand-blue);
  }
  .divider--first { left: 514px; }
  .divider--second { left: 735px; }
  .address {
    position: absolute;
    left: 529px; top: 68px;
    font-size: 16px;
    line-height: 22.6px;
    font-style: normal;
  }
  .contacts {
    position: absolute;
    left: 757px; top: 68px;
    list-style: none;
    font-size: 16px;
    line-height: 22.6px;
  }
  .contacts li { display: flex; align-items: center; gap: 8px; }
  .contacts svg { width: 16px; height: 16px; flex: none; }
  .rule {
    position: absolute;
    left: 0; top: 177px;
    width: 100%; height: 2px;
    background: var(--brand-blue);
  }
  .disclaimer {
    position: absolute;
    left: 0; top: 179px;
    width: 100%; height: 116px;
    background: var(--band);
    padding: 15px 38px 0 38px;
    font-size: 14px;
    line-height: 22.8px;
  }
  .disclaimer-line {
    display: block;
    white-space: nowrap;
    text-align: justify;
    text-align-last: justify;
  }
  .disclaimer-line--last { text-align-last: left; }
</style>
</head>
<body>
  <section class="signature">
    <div class="brand">
      <span class="brand-dot"></span>
      <span class="brand-name">Tidewell Auto Leasing</span>
    </div>

    <div class="role">
      <p class="role-title">Customer Service</p>
      <p class="role-company">Tidewell Auto Leasing</p>
    </div>

    <span class="divider divider--first"></span>

    <address class="address">
      P.O.Box 512<br>
      Seaview Town KY1-2040<br>
      CAYMAN ISLANDS
    </address>

    <span class="divider divider--second"></span>

    <ul class="contacts">
      <li>
        <svg viewBox="0 0 24 24" aria-hidden="true"><path fill="#0a4fc9" d="M6.6 10.8a15.1 15.1 0 0 0 6.6 6.6l2.2-2.2a1 1 0 0 1 1-.25 11.4 11.4 0 0 0 3.6.57 1 1 0 0 1 1 1V20a1 1 0 0 1-1 1A17 17 0 0 1 3 4a1 1 0 0 1 1-1h3.5a1 1 0 0 1 1 1c0 1.25.2 2.45.57 3.57a1 1 0 0 1-.25 1z"/><path fill="none" stroke="#0a4fc9" stroke-width="1.8" d="M14 3.5a7 7 0 0 1 6.5 6.5M14 7a3.5 3.5 0 0 1 3 3"/></svg>
        345-555-0142
      </li>
      <li>
        <svg viewBox="0 0 24 24" aria-hidden="true"><rect x="1" y="4" width="22" height="16" rx="1" fill="#0a4fc9"/><path d="M2 5l10 8 10-8" fill="none" stroke="#fff" stroke-width="2"/></svg>
        service@tidewell.ky
      </li>
      <li>
        <svg viewBox="0 0 24 24" aria-hidden="true"><g fill="none" stroke="#0a4fc9" stroke-width="1.8"><circle cx="12" cy="12" r="10"/><ellipse cx="12" cy="12" rx="4.5" ry="10"/><path d="M2 12h20M4 6.5h16M4 17.5h16"/></g></svg>
        tidewell.ky
      </li>
    </ul>

    <div class="rule"></div>

    <p class="disclaimer">
      <span class="disclaimer-line">This e-mail from service@tidewellautoleasing.com and any files transmitted with it are confidential and intended solely for the</span>
      <span class="disclaimer-line">use of the individual or entity to whom they are addressed. If you are not the intended recipient or have received this email in</span>
      <span class="disclaimer-line">error, please notify service@tidewellautoleasing.com destroy and delete any copies you have received without disclosure,</span>
      <span class="disclaimer-line disclaimer-line--last">copying, distribution or taking action in reliance of the contents of this communication.</span>
    </p>
  </section>
</body>
</html>
```